professional looking data specialist website

I've recently had a new logo designed and I'm now looking to get a professional looking website built. This is for a new company that specialises in data. We look to support companies with business intelligence, report modelling, data governance to new european legislation (GDPR). We are offer consultancy or we can attend site and complete work when required. Our target arket is united kingdom wide and we are specifically aiming at small to medium sized companies.

Target Market(s)

small to medium enterprise companies from all industries

Industry/Entity Type

Professional Service

Coding

Coded - Design and coding required

Number of Pages Required

4 page

Font styles to use
Sans Serif

Colors

Designer to choose colors to be used in the design.

Requirements
Must have
• Professional look including the company logo, need to have ability to request more information from us so needs a inquiries page, seperate pages for the different offerings, data governance, report modelling, business intelligence implementation, data protection
Nice to have
• any website interaction, animation, etc
Should not have
• too many colours, too busy pages, must look professional

```html
<!DOCTYPE html>
<html lang="en">
<head>
<meta charset="utf-8">
<title>Harlow Data Ltd – Contact</title>
<link rel="stylesheet" href="https://fonts.googleapis.com/css2?family=Josefin+Sans:wght@300;400&display=swap">
<style>
:root{
  --ink-dark:#232e36;
  --ink-dark-soft:#3b4f5d;
  --slate:#5a7685;
  --card:#d8d8d8;
  --card-text:#2a2a2a;
  --white:#ffffff;
  --teal-light:#9fd3e4;
  --field:#7d919b;
  --field-border:#5f9bb2;
  --maroon:#7a1e35;
}
*{margin:0;padding:0;box-sizing:border-box}
html,body{width:936px;height:1200px;overflow:hidden}
body{position:relative;font-family:"Josefin Sans",sans-serif;font-weight:300;background:var(--slate);color:var(--white)}
.abs{position:absolute}

/* services strip */
.services{left:0;top:0;width:936px;height:155px;background:var(--ink-dark)}
.services .corner{left:0;top:0}
.service-card{top:-20px;width:251px;height:102px;background:var(--card);color:var(--card-text);padding:20px 22px 0;font-size:9px;line-height:13px;font-weight:300}
.service-card .read-more{display:block;margin-top:22px;font-size:10px}
.service-card .read-more::after{content:"›";font-weight:400;font-size:14px;margin-left:4px}

/* testimonials */
.testimonials{left:0;top:155px;width:936px;height:334px;
  background:radial-gradient(ellipse at 50% 40%,#4a6576 0%,#3c5566 45%,#2e4452 100%)}
.section-title{left:0;width:936px;text-align:center;font-weight:400;font-size:34px;letter-spacing:8.4px;padding-left:8px;white-space:nowrap}
.section-sub{left:0;width:936px;text-align:center;font-size:16px;letter-spacing:3.6px;color:var(--teal-light);font-weight:400}
.rule{height:1px;background:var(--ink-dark)}
.quote-mark{left:0;width:936px;text-align:center;font-size:60px;font-weight:400;line-height:1}
.quote-text{left:0;width:936px;text-align:center;font-size:21px;line-height:29px}
.avatar{left:434px;width:68px;height:68px;border-radius:50%;border:2px solid var(--maroon);
  background:linear-gradient(135deg,#b59a86,#6e4a3e)}

/* contact */
.map{left:0;top:683px;width:936px;height:197px;background:linear-gradient(90deg,#cfe0b8 0%,#d5ddd2 30%,#d7ddd5 100%)}
.contact-item{left:84px;width:340px;display:flex;gap:20px;font-size:13px;letter-spacing:2.2px;line-height:17px;font-weight:300;white-space:nowrap}
.contact-item svg{flex:none}
.field{border:1px solid var(--field-border);background:var(--field);border-radius:5px;font-size:13px;letter-spacing:3px;font-weight:400;color:#e8eef1}
.field.center{display:flex;align-items:center;justify-content:center}
.send{left:769px;top:1041px;width:81px;height:28px;border-radius:14px;border:1px solid var(--field-border);background:var(--slate);
  display:flex;align-items:center;justify-content:center;font-size:15px;letter-spacing:3px;color:var(--teal-light);font-weight:400}
.policy-links{left:84px;top:1106px;width:768px;display:flex;justify-content:space-between;font-size:12px;letter-spacing:2px;font-weight:400;white-space:nowrap}
.policy-links a{color:var(--teal-light);text-decoration:underline;text-underline-offset:3px}

/* footer */
.site-footer{left:0;top:1144px;width:936px;height:56px;background:var(--ink-dark)}
.copyright{left:84px;top:22px;font-size:11.5px;letter-spacing:0.4px;color:var(--teal-light);font-weight:400;white-space:nowrap}
.to-top{left:409px;top:0}
</style>
</head>
<body>

<section class="abs services">
  <svg class="abs corner" width="64" height="64"><polygon points="0,0 64,0 0,64" fill="var(--ink-dark-soft)"/></svg>
  <article class="abs service-card" style="left:84px">ornare vitae blandit sed, mollis pulvinar<br>tortor...<a class="read-more">Read More</a></article>
  <article class="abs service-card" style="left:343px">ornare vitae blandit sed, mollis pulvinar<br>tortor...<a class="read-more">Read More</a></article>
  <article class="abs service-card" style="left:600px">ornare vitae blandit sed, mollis pulvinar<br>tortor...<a class="read-more">Read More</a></article>
</section>

<section class="abs testimonials" role="img" aria-label="Blurred photograph of a data centre aisle with server racks">
</section>
<h2 class="abs section-title" style="top:176px">WHAT CLIENTS SAY?</h2>
<div class="abs rule" style="left:198px;top:231px;width:182px"></div>
<div class="abs rule" style="left:558px;top:231px;width:183px"></div>
<p class="abs section-sub" style="top:222px">TESTIMONIALS</p>
<div class="abs quote-mark" style="top:252px">“</div>
<p class="abs quote-text" style="top:310px">Lorem ipsum dolor sit amet, consectetur adipiscing elit.<br>Curabitur tortor quam, scelerisque eu purus eu, auctor dictum nibh.</p>
<div class="abs avatar" style="top:394px" role="img" aria-label="Portrait photo of the client giving the testimonial"></div>

<h2 class="abs section-title" style="top:584px">LET’S GET CONNECTED</h2>
<div class="abs rule" style="left:197px;top:638px;width:182px"></div>
<div class="abs rule" style="left:558px;top:638px;width:182px"></div>
<p class="abs section-sub" style="top:629px">CONTACT US</p>

<div class="abs map" role="img" aria-label="Street map showing the office location with a red pin"></div>

<div class="abs contact-item" style="top:924px">
  <svg width="26" height="26" viewBox="0 0 26 26" fill="none" stroke="#fff" stroke-width="1.2"><path d="M13 3a6 6 0 0 1 6 6c0 5-6 11-6 11S7 14 7 9a6 6 0 0 1 6-6z"/><circle cx="13" cy="9" r="2.2"/><path d="M8 18c-4 1-5 2-5 3 0 1.5 4.5 2.5 10 2.5S23 22.5 23 21c0-1-1-2-5-3"/></svg>
  <span style="margin-top:-3px">Adress line one, line two<br>street name, location name, country<br>pincode</span>
</div>
<div class="abs contact-item" style="top:991px">
  <svg width="26" height="20" viewBox="0 0 26 20" fill="none" stroke="#fff" stroke-width="1.2"><rect x="1" y="3" width="24" height="15"/><path d="M1 3l12 9 12-9M1 18l9-7M25 18l-9-7"/></svg>
  <span style="margin-top:3px">info@harlowdata.com</span>
</div>
<div class="abs contact-item" style="top:1027px">
  <svg width="26" height="26" viewBox="0 0 26 26" fill="none" stroke="#fff" stroke-width="1.2"><path d="M5 2l4 5-2 3c1 3 4 6 7 8l3-2 5 4-3 4C10 23 2 14 2 5z"/></svg>
  <span style="margin-top:0">(0123) 555 010</span>
</div>

<div class="abs field center" style="left:437px;top:922px;width:198px;height:29px">YOUR NAME</div>
<div class="abs field center" style="left:654px;top:922px;width:196px;height:29px">EMAIL</div>
<div class="abs field" style="left:437px;top:963px;width:413px;height:65px;padding:13px 13px">MESSAGE...</div>
<div class="abs send">SEND</div>

<nav class="abs policy-links">
  <a>PRIVACY POLICY</a><a>HIPPA STATEMENT</a><a>LANGUAGE ASSISTANCE</a><a>NON-DISCRIMINATION NOTICE</a>
</nav>

<footer class="abs site-footer">
  <p class="abs copyright">© HARLOW DATA LTD 2017. ALL RIGHTS RESERVED</p>
  <svg class="abs to-top" width="118" height="56" viewBox="0 0 118 56">
    <polygon points="59,0 118,56 0,56" fill="var(--slate)"/>
    <polyline points="34,56 59,34 84,56" fill="none" stroke="var(--teal-light)" stroke-width="7"/>
  </svg>
</footer>

</body>
</html>
```